Gadgetry Glamour Business Card

we are selling techies and beauties stuffs online and store line.
will be expanding into craft products, specifically handmade products,
therefore i want my name card / business card designs to be crafty , carton box look a like, with colour theme from "tradio logo" because that will be our main base of operations, if possible, do a little logo of "visit store" as it looks like from tradio, as well as tradio logo on the business card. Please as well leave a line for me to stick my website sticker on it once i've got my website set up in the future.

 i want my business card to have yellowish brown (carton box lookalike) color as a base, while the rest will be based on tradio's logo color theme. thank you.

Industry/Entity Type

Store

Contact Information for Business Card

-for your everyday techie and beauty needs -

Gadgetry Glamour

R.M. Dov
41, Wexmoor Crescent,
Brightvale East, Victoria 3087
Australia

Colors
eb1f27
0255a3
fbed22
9bcb3c

Requirements
Must have
• a carton box cut-out lookalike

```html
<!DOCTYPE html>
<html lang="en">
<head>
<meta charset="utf-8">
<title>Gadgetry Glamour Business Card</title>
<link rel="stylesheet" href="https://fonts.googleapis.com/css2?family=Josefin+Sans:wght@300;400&family=Open+Sans:wght@800&family=Sofia&display=swap">
<style>
  :root {
    --backdrop: #6f7c0b;
    --kraft: #c8a478;
    --kraft-light: #d2b085;
    --ink: #1c1a18;
    --emblem: #141414;
    --marketplace: #0255a3;
    --shadow: rgba(30, 35, 0, 0.55);
  }
  * { margin: 0; padding: 0; box-sizing: border-box; }
  html, body { width: 900px; height: 1200px; overflow: hidden; }
  body { background: var(--backdrop); position: relative; }

  .card {
    position: absolute;
    left: 30px;
    width: 842px;
    height: 515px;
    background: radial-gradient(ellipse at 40% 35%, var(--kraft-light), var(--kraft) 75%);
    box-shadow: 12px 14px 14px var(--shadow);
  }
  .card--front { top: 30px; }
  .card--back { top: 655px; height: 513px; }

  .cut-frame { position: absolute; left: 0; top: 0; width: 842px; height: 100%; }

  .address {
    position: absolute;
    top: 42px; left: 0; width: 842px;
    text-align: center;
    font-family: "Josefin Sans", sans-serif;
    font-weight: 300;
    font-size: 18px;
    white-space: nowrap;
    color: var(--ink);
  }
  .emblem { position: absolute; border-radius: 50%; background: var(--emblem); }
  .card--front .emblem { left: 310px; top: 84px; width: 236px; height: 236px; }
  .card--back .emblem { left: 285px; top: 44px; width: 286px; height: 286px; }

  .tagline {
    position: absolute;
    top: 345px; left: 0; width: 842px;
    text-align: center;
    font-family: "Josefin Sans", sans-serif;
    font-size: 27px;
    color: var(--ink);
  }
  .store-call {
    position: absolute;
    left: 50px; top: 398px;
    font-family: "Open Sans", sans-serif;
    font-weight: 800;
    font-size: 18px;
    line-height: 26px;
    color: var(--ink);
  }
  .marketplace {
    position: absolute;
    left: 150px; top: 418px;
    font-family: "Josefin Sans", sans-serif;
    font-size: 30px;
    color: var(--marketplace);
  }
  .website-slot {
    position: absolute;
    left: 274px; top: 423px;
    width: 292px; height: 28px;
    border: 2px dashed var(--ink);
    text-align: center;
    font-family: "Josefin Sans", sans-serif;
    font-weight: 300;
    font-size: 15px;
    line-height: 26px;
    color: var(--ink);
  }
  .brand-name {
    position: absolute;
    left: 0; top: 336px; width: 842px;
    text-align: center;
    font-family: "Sofia", cursive;
    font-size: 84px;
    white-space: nowrap;
    color: var(--ink);
  }
</style>
</head>
<body>

<section class="card card--front">
  <svg class="cut-frame" viewBox="0 0 842 515" aria-hidden="true">
    <rect x="31" y="31" width="782" height="458" fill="none" stroke="#111" stroke-width="8" stroke-dasharray="30 13"/>
  </svg>
  <p class="address">Gadgetry Glamour R.M. Dov 41, Wexmoor Crescent, Brightvale East, Victoria 3087 Australia</p>
  <div class="emblem" role="img" aria-label="Space for the brand emblem"></div>
  <p class="tagline">For your everyday techie and beauty needs.</p>
  <p class="store-call">VISIT<br>OUR<br>STORE</p>
  <p class="marketplace">tradio</p>
  <p class="website-slot">website goes here</p>
</section>

<section class="card card--back">
  <svg class="cut-frame" viewBox="0 0 842 513" aria-hidden="true">
    <rect x="31" y="29" width="782" height="456" fill="none" stroke="#111" stroke-width="8" stroke-dasharray="30 13"/>
  </svg>
  <div class="emblem" role="img" aria-label="Space for the brand emblem"></div>
  <p class="brand-name">GadgetryGlamour</p>
</section>

</body>
</html>
```